EPIC, awesome, creative business card needed - get involved!

I'm launching a boutique, exclusive Property Management real estate agency in Sydney early next year.
The name of the agency will be called "Silver Oak Lane" - it's a play on "follow the yellow brick road" to wealth. The Silver Oak Lane signifies wealth through property investment.
My business will offer management of investment properties (ie Property Management).
The difference with Silver Oak Lane and other agencies is the business will be run by one of Australia's leading property investment experts, and also one of Australia's leading property managers.
It will be exclusively for high net worth properties and individuals, so the business card needs to be extremely sharp, slick and relatively simple.
The information I want on the card is as follows
Marcus Fenwick - Director
M: 0471 926 154
P: 9637 0518
E: marcus@silveroaklane.net.au
W: silveroaklane.net.au
I'm happy with the red from the logo, black - no yellows or funky colors. I want this to be a super corporate and slick business card to match the high end nature of the business.
Good luck everyone, and please ask questions for clarification.

```html
<!DOCTYPE html>
<html lang="en">
<head>
<meta charset="utf-8">
<title>Silver Oak Lane – Business Card</title>
<link rel="stylesheet" href="https://fonts.googleapis.com/css2?family=Open+Sans:wght@400;700&display=swap">
<style>
  :root {
    --backdrop: #ececec;
    --front-start: #4b1d1e;
    --front-end: #1a0b0e;
    --card-white: #ffffff;
    --card-shade: #e3e1dc;
    --brand-red: #f0383c;
    --ink: #2a2a2a;
    --ink-soft: #6d6d6d;
  }
  * { box-sizing: border-box; margin: 0; padding: 0; }
  html, body {
    width: 1200px; height: 1000px; overflow: hidden;
    background: var(--backdrop);
    font-family: "Open Sans", Arial, sans-serif;
  }
  .canvas { position: relative; width: 1200px; height: 1000px; }
  .card {
    position: absolute; left: 347px; width: 530px; height: 306px;
    border-radius: 22px;
  }
  .card--front {
    top: 147px;
    background: linear-gradient(135deg, var(--front-start) 0%, var(--front-end) 100%);
    display: flex; align-items: center; justify-content: center;
  }
  .card--back {
    top: 535px;
    background: linear-gradient(135deg, var(--card-white) 62%, var(--card-shade) 100%);
  }
  .brand {
    display: flex; align-items: flex-start; gap: 8px;
    color: var(--brand-red);
    font-weight: 700; text-transform: uppercase;
    letter-spacing: 0.5px;
  }
  .brand__square { background: var(--brand-red); flex: none; }
  .brand__name { display: block; }
  .card--front .brand { font-size: 22px; line-height: 26px; }
  .card--front .brand__square { width: 15px; height: 15px; margin-top: 5px; }
  .card--back .brand {
    position: absolute; left: 70px; top: 100px;
    font-size: 28px; line-height: 34px;
  }
  .card--back .brand__square { width: 19px; height: 19px; margin-top: 7px; }
  .person { position: absolute; left: 280px; top: 84px; }
  .person__name { font-size: 19px; color: var(--ink); line-height: 24px; }
  .person__role { font-size: 10px; color: var(--ink-soft); line-height: 12px; }
  .details {
    position: absolute; left: 264px; top: 143px;
    list-style: none; font-size: 16px; line-height: 20px; color: var(--ink);
  }
  .details__item { display: flex; align-items: center; gap: 5px; }
  .details__icon { width: 12px; height: 12px; flex: none; fill: var(--ink); }
  .details__label { width: 12px; font-size: 12px; font-weight: 700; text-align: center; }
</style>
</head>
<body>
<main class="canvas">
  <section class="card card--front">
    <div class="brand">
      <span class="brand__square"></span>
      <span class="brand__name">Silver<br>Oak<br>Lane</span>
    </div>
  </section>

  <section class="card card--back">
    <div class="brand">
      <span class="brand__square"></span>
      <span class="brand__name">Silver<br>Oak<br>Lane</span>
    </div>

    <div class="person">
      <p class="person__name">Marcus Fenwick</p>
      <p class="person__role">Director</p>
    </div>

    <ul class="details">
      <li class="details__item">
        <svg class="details__icon" viewBox="0 0 24 24"><path d="M6.6 10.8a15.1 15.1 0 0 0 6.6 6.6l2.2-2.2c.3-.3.7-.4 1-.2 1.1.4 2.3.6 3.6.6.6 0 1 .4 1 1V20c0 .6-.4 1-1 1C10.6 21 3 13.4 3 4c0-.6.4-1 1-1h3.5c.6 0 1 .4 1 1 0 1.3.2 2.5.6 3.6.1.3 0 .7-.2 1z"/></svg>
        <span>0471 926 154</span>
      </li>
      <li class="details__item">
        <svg class="details__icon" viewBox="0 0 24 24"><path d="M6.6 10.8a15.1 15.1 0 0 0 6.6 6.6l2.2-2.2c.3-.3.7-.4 1-.2 1.1.4 2.3.6 3.6.6.6 0 1 .4 1 1V20c0 .6-.4 1-1 1C10.6 21 3 13.4 3 4c0-.6.4-1 1-1h3.5c.6 0 1 .4 1 1 0 1.3.2 2.5.6 3.6.1.3 0 .7-.2 1z"/></svg>
        <span>9637 0518</span>
      </li>
      <li class="details__item">
        <svg class="details__icon" viewBox="0 0 24 24"><path d="M2 5h20L12 12.5z M2 7.2l10 7.8 10-7.8V19H2z"/></svg>
        <span>marcus@silveroaklane.net.au</span>
      </li>
      <li class="details__item">
        <span class="details__label">W</span>
        <span>silveroaklane.net.au</span>
      </li>
    </ul>
  </section>
</main>
</body>
</html>
```